Software company WebSite Design (enterprise level SW, Mobile apps, HW prototypes)

We need design for our new webpages. We got new logo and new business cards and we need webdesign which will be match with those two.
We are dealing with corporate level software development - enterprise level portals, development of optimalization SW, route planning optimalizations. For a few months we are developing mobile applications for companies.
IMPORTANT is to express the cutting edge technological company.

Target Market(s)

IT company customers

Industry/Entity Type

Business

Number of Pages Required

2 page

Requirements
Must have
• Project needs to have landing page and product detail page. Design needs to be created including full font and example images as there would be a real webpage. Design should be clean, modern and expressing hi-tech level of the company.
• Example of well designer web pages - www.quorvelt.com, www.brandissa.com - We like the font formatting and font designs (colors, placing, etc - its professional).
• Attached image contains screenshot from old web landing page. It contains basic sections of our business (Simulation Tools, Enterprise Intranet Systems, Hi-tech web presentations, Supporting Enterprise services - Optimalization and logistics monitoring)

```html
<!DOCTYPE html>
<html lang="en">
<head>
<meta charset="utf-8">
<title>Qorda Solutions</title>
<link rel="stylesheet" href="https://fonts.googleapis.com/css2?family=Rajdhani:wght@500;600;700&family=Lato:wght@400;700&family=Montserrat:wght@500;600;700&display=swap">
<style>
:root{
  --blue:#1a8fd6;
  --blue-dark:#0d6fb3;
  --cyan:#2fb4e8;
  --orange:#f07a1f;
  --orange-dark:#d95a12;
  --ink:#1d1d1d;
  --text:#3a3a3a;
  --muted:#6b6b6b;
  --light:#f4f5f6;
  --grey:#ececec;
  --footer:#222325;
  --footer-dark:#141414;
  --line:#d8d8d8;
}
*{box-sizing:border-box;margin:0;padding:0}
html,body{width:1200px;height:2791px;overflow:hidden;background:#fff}
body{position:relative;font-family:"Lato",sans-serif;color:var(--text)}
.abs{position:absolute}

/* header */
.site-header{position:absolute;left:0;top:0;width:1200px;height:102px;background:#fff}
.brand{position:absolute;left:164px;top:30px;display:flex;align-items:center;gap:12px}
.brand-square{width:36px;height:36px;background:var(--blue)}
.brand-name{font-family:"Rajdhani",sans-serif;font-weight:700;font-size:34px;color:#3b3b3b;letter-spacing:1px}
.top-contact{position:absolute;top:14px;display:flex;align-items:center;gap:10px;font-family:"Montserrat",sans-serif;font-size:12px;color:#333}
.top-contact .chip{width:30px;height:30px;background:var(--blue-dark);transform:rotate(45deg);border-radius:6px;display:flex;align-items:center;justify-content:center}
.top-contact .chip svg{transform:rotate(-45deg)}
.main-nav{position:absolute;top:56px;left:470px;display:flex;font-family:"Rajdhani",sans-serif;font-weight:600;font-size:17px;color:#222}
.main-nav a{color:inherit;text-decoration:none;padding:0 22px;border-left:1px solid #bbb;line-height:18px}
.main-nav a:first-child{border-left:none;color:var(--blue)}

/* hero */
.hero{position:absolute;left:0;top:102px;width:1200px;height:545px;overflow:hidden;
  background:linear-gradient(100deg,#dfe9ef 0%,#a9c6d6 35%,#cfe0e9 60%,#e6eef2 100%)}
.hero-badge{position:absolute;left:192px;top:204px;width:270px;height:270px;background:rgba(20,120,190,.88);transform:rotate(45deg);border-radius:40px}
.hero-title{position:absolute;left:186px;top:182px;width:430px;text-align:center;font-family:"Rajdhani",sans-serif;font-weight:600;font-size:31px;line-height:39px;color:#fff}
.hero-arrow{position:absolute;top:243px}

/* section headings */
.section-title{position:absolute;left:0;width:1200px;text-align:center;font-family:"Rajdhani",sans-serif;font-weight:600;font-size:37px;color:var(--ink);letter-spacing:.5px}
.section-title span{color:var(--blue)}
.divider{position:absolute;left:540px;width:120px;height:12px}

/* services */
.services{position:absolute;left:0;top:647px;width:1200px;height:482px;background:var(--light)}
.service{position:absolute;width:230px;text-align:center}
.service-icon{position:relative;width:160px;height:160px;margin:0 auto}
.service-icon .back{position:absolute;left:30px;top:30px;width:100px;height:100px;transform:rotate(45deg);border-radius:20px;opacity:.35}
.service-icon .front{position:absolute;left:38px;top:38px;width:84px;height:84px;transform:rotate(45deg);border-radius:16px}
.service-icon svg{position:absolute;left:58px;top:58px}
.service-label{margin-top:30px;font-family:"Rajdhani",sans-serif;font-weight:600;font-size:20px;line-height:24px;color:var(--ink)}

/* about */
.about{position:absolute;left:0;top:1129px;width:1200px;height:545px;background:#fff}
.about-copy{position:absolute;left:166px;top:118px;width:870px;text-align:center;font-size:11.5px;line-height:21.5px;color:#444}
.about-copy p{margin-bottom:21px}

/* features */
.features{position:absolute;left:0;top:1674px;width:1200px;height:409px;background:var(--grey)}
.feature{position:absolute;width:380px;height:104px;background:#fff}
.feature h3{font-family:"Rajdhani",sans-serif;font-weight:600;font-size:20px;letter-spacing:.3px}
.feature p{font-family:"Montserrat",sans-serif;font-weight:600;font-size:11.5px;line-height:19px;color:#555}
.feature .blue{color:var(--blue)}
.feature .dark{color:var(--ink)}
.more{position:absolute;display:flex;height:22px;font-family:"Montserrat",sans-serif;font-size:10px;font-weight:600}
.more .plus{width:26px;background:var(--blue);color:#fff;text-align:center;line-height:22px;font-size:16px}
.more .label{width:66px;background:#d9d9d9;color:#fff;line-height:22px;text-align:center}
.plus-box{position:absolute;width:22px;height:22px;background:#fff;border:1px solid #ddd;text-align:center;line-height:20px;font-size:15px;color:#333}
.center-brand{position:absolute;left:530px;top:130px;width:140px;text-align:center}
.center-brand .sq{width:80px;height:80px;background:var(--blue);margin:0 auto 12px;transform:rotate(45deg)}
.center-brand .name{font-family:"Rajdhani",sans-serif;font-weight:700;font-size:34px;color:#3b3b3b}

/* projects */
.projects{position:absolute;left:0;top:2083px;width:1200px;height:406px;background:#fff}
.project-strip{position:absolute;left:164px;top:168px;width:874px;height:240px;background:#f2f2f2;box-shadow:0 10px 18px -12px rgba(0,0,0,.35)}
.project{position:absolute;top:10px;width:180px;text-align:center}
.project .shot{width:180px;height:92px}
.project p{margin-top:12px;font-family:"Montserrat",sans-serif;font-weight:600;font-size:11px;line-height:17px;color:#333}
.strip-arrow{position:absolute;top:48px;width:22px;height:22px;border-radius:50%;background:#ddd}

/* footer */
.site-footer{position:absolute;left:0;top:2489px;width:1200px;height:264px;background:var(--footer);color:#ccc}
.footer-col{position:absolute;top:42px}
.footer-col h4{font-family:"Rajdhani",sans-serif;font-weight:700;font-size:16px;color:#fff;padding-bottom:6px;border-bottom:1px solid var(--orange);display:inline-block;min-width:100%}
.quick-links{list-style:none;margin-top:18px;font-family:"Montserrat",sans-serif;font-size:10px;font-weight:600;color:#ddd}
.quick-links li{margin-bottom:14px}
.quick-links li::before{content:"\2022";margin-right:6px;color:var(--orange)}
.quick-links li.active{color:var(--orange)}
.contact-line{display:flex;gap:16px;margin-top:18px;font-size:10.5px;line-height:15px;color:#ccc}
.field{width:250px;height:24px;background:#3a3b3d;margin-bottom:6px;font-size:10.5px;color:#ddd;padding:5px 8px}
.field.msg{height:46px}
.submit{width:90px;height:24px;background:var(--orange);border-radius:3px;color:#fff;font-family:"Montserrat",sans-serif;font-weight:700;font-size:11px;line-height:24px;padding-left:30px}
.footer-brand{position:absolute;left:874px;top:106px;display:flex;align-items:center;gap:10px}
.footer-brand .sq{width:28px;height:28px;background:#8a8a8a}
.footer-brand .name{font-family:"Rajdhani",sans-serif;font-weight:700;font-size:28px;color:#bbb}
.social{position:absolute;left:918px;top:192px;display:flex;gap:10px}
.social span{width:22px;height:22px;border:1.5px solid var(--orange);border-radius:50%}
.copyright{position:absolute;left:0;top:2753px;width:1200px;height:38px;background:var(--footer-dark);color:#ccc;font-size:10px;text-align:center;line-height:38px}
</style>
</head>
<body>

<header class="site-header">
  <div class="brand"><span class="brand-square"></span><span class="brand-name">QORDA</span></div>
  <div class="top-contact" style="left:734px">
    <span class="chip"><svg width="14" height="10" viewBox="0 0 14 10"><rect x="0.5" y="0.5" width="13" height="9" fill="none" stroke="#fff"/><path d="M0.5 0.5 L7 5.5 L13.5 0.5" fill="none" stroke="#fff"/></svg></span>
    info@qordamail.com
  </div>
  <div class="top-contact" style="left:910px;font-size:13px">
    <span class="chip"><svg width="12" height="12" viewBox="0 0 12 12"><path d="M2 1 L4.5 1 L5.5 4 L4 5 Q5 7.5 7 8 L8 6.5 L11 7.5 L11 10 Q5 11 1 3 Z" fill="#fff"/></svg></span>
    (123) 456 7890
  </div>
  <nav class="main-nav">
    <a href="#">HOME</a><a href="#">SERVICES</a><a href="#">ABOU US</a><a href="#">RESOURCES</a><a href="#">CONTACT US</a>
  </nav>
</header>

<section class="hero">
  <div class="abs" role="img" aria-label="Woman in white working on a holographic touch interface in a futuristic light blue office" style="left:0;top:0;width:1200px;height:545px"></div>
  <div class="hero-badge"></div>
  <h1 class="hero-title">Everything You Need Great Enterprise Level Software, Mobile Apps, Hardware Prototypes.</h1>
  <svg class="hero-arrow" style="left:30px" width="24" height="56" viewBox="0 0 24 56"><path d="M22 2 L4 28 L22 54" fill="none" stroke="#6d8794" stroke-width="6"/></svg>
  <svg class="hero-arrow" style="left:1150px" width="24" height="56" viewBox="0 0 24 56"><path d="M2 2 L20 28 L2 54" fill="none" stroke="#1f2a30" stroke-width="6"/></svg>
</section>

<section class="services">
  <h2 class="section-title" style="top:42px"><span>OUR</span> SERVICES</h2>
  <svg class="divider" style="top:100px" viewBox="0 0 120 12"><line x1="0" y1="6" x2="52" y2="6" stroke="#ccc"/><line x1="68" y1="6" x2="120" y2="6" stroke="#ccc"/><rect x="55" y="1" width="10" height="10" transform="rotate(45 60 6)" fill="none" stroke="#bbb"/></svg>

  <div class="service" style="left:132px;top:158px">
    <div class="service-icon">
      <div class="back" style="background:#f4b58a"></div>
      <div class="front" style="background:var(--blue-dark)"></div>
      <svg width="44" height="44" viewBox="0 0 44 44"><g fill="none" stroke="#fff" stroke-width="2"><circle cx="22" cy="22" r="16"/><ellipse cx="22" cy="22" rx="7" ry="16"/><line x1="6" y1="22" x2="38" y2="22"/><path d="M9 14 H35 M9 30 H35"/></g></svg>
    </div>
    <div class="service-label">Enterprise Level<br>Portals</div>
  </div>
  <div class="service" style="left:367px;top:158px">
    <div class="service-icon">
      <div class="back" style="background:#f4b58a"></div>
      <div class="front" style="background:var(--cyan)"></div>
      <svg width="44" height="44" viewBox="0 0 44 44"><g fill="none" stroke="#fff" stroke-width="2.2"><rect x="14" y="6" width="16" height="30" rx="2"/><line x1="19" y1="31" x2="25" y2="31"/><path d="M8 14 L4 22 L8 30 M36 14 L40 22 L36 30"/></g></svg>
    </div>
    <div class="service-label">Development of<br>Optimalization Softwares</div>
  </div>
  <div class="service" style="left:601px;top:158px">
    <div class="service-icon">
      <div class="back" style="background:#9fc9ea"></div>
      <div class="front" style="background:var(--orange-dark)"></div>
      <svg width="44" height="44" viewBox="0 0 44 44"><g fill="none" stroke="#fff" stroke-width="2.2"><path d="M30 20 C24 12 24 6 30 6 C36 6 36 12 30 20 Z"/><circle cx="30" cy="11" r="2"/><path d="M30 22 C30 30 12 24 12 32 C12 36 20 38 26 38"/><circle cx="10" cy="34" r="3"/></g></svg>
    </div>
    <div class="service-label">Route Planning<br>Optimalization</div>
  </div>
  <div class="service" style="left:835px;top:158px">
    <div class="service-icon">
      <div class="back" style="background:#9fc9ea"></div>
      <div class="front" style="background:var(--orange)"></div>
      <svg width="44" height="44" viewBox="0 0 44 44"><g fill="none" stroke="#fff" stroke-width="2.2"><rect x="8" y="6" width="18" height="32" rx="2"/><circle cx="28" cy="22" r="6"/><path d="M28 12 V15 M28 29 V32 M18 22 H21 M35 22 H38 M21 15 L23 17 M33 27 L35 29 M35 15 L33 17"/></g></svg>
    </div>
    <div class="service-label">Developing Mobile<br>Applications For<br>Companies</div>
  </div>
</section>

<section class="about">
  <h2 class="section-title" style="top:22px"><span>ABOUT</span> QORDA SOLUTIONS</h2>
  <svg class="divider" style="top:80px" viewBox="0 0 120 12"><line x1="0" y1="6" x2="52" y2="6" stroke="#ccc"/><line x1="68" y1="6" x2="120" y2="6" stroke="#ccc"/><rect x="55" y="1" width="10" height="10" transform="rotate(45 60 6)" fill="none" stroke="#bbb"/></svg>
  <div class="about-copy">
    <p>Sed ut perspiciatis unde omnis iste natus error sit voluptatem accusantium doloremque laudantium, totam rem aperiam, eaque ipsa quae ab illo inventore veritatis et quasi architecto beatae vitae dicta sunt explicabo. Nemo enim ipsam voluptatem quia voluptas sit aspernatur aut odit aut fugit, sed quia consequuntur magni dolores eos qui ratione voluptatem sequi nesciunt. Neque porro quisquam est, qui dolorem ipsum quia dolor sit amet, consectetur, adipisci velit, sed quia non numquam eius modi tempora incidunt ut labore et dolore magnam aliquam quaerat voluptatem. Ut enim ad minima veniam, quis nostrum exercitationem ullam corporis suscipit laboriosam, nisi ut aliquid ex ea commodi consequatur? Quis autem vel eum iure reprehenderit qui in ea voluptate velit esse quam nihil molestiae consequatur, vel illum qui dolorem eum fugiat quo voluptas nulla pariatur. Sed ut perspiciatis unde omnis iste natus error sit voluptatem accusantium doloremque laudantium, totam rem aperiam, eaque ipsa quae ab illo inventore veritatis et quasi architecto beatae vitae dicta sunt explicabo. Nemo enim ipsam voluptatem quia voluptas sit aspernatur aut odit aut fugit, sed quia consequuntur magni dolores eos qui ratione voluptatem sequi nesciunt.</p>
    <p>Neque porro quisquam est, qui dolorem ipsum quia dolor sit amet, consectetur, adipisci velit, sed quia non numquam eius modi tempora incidunt ut labore et dolore magnam aliquam quaerat voluptatem. Ut enim ad minima veniam, quis nostrum exercitationem ullam corporis suscipit laboriosam, nisi ut aliquid ex ea commodi consequatur? Quis autem vel eum iure reprehenderit qui in ea voluptate velit esse quam nihil molestiae consequatur, vel illum qui dolorem eum fugiat quo voluptas.</p>
    <p>Neque porro quisquam est, qui dolorem ipsum quia dolor sit amet, consectetur, adipisci velit, sed quia non numquam eius modi tempora incidunt ut labore et dolore magnam aliquam quaerat voluptatem. Ut enim ad minima veniam, quis nostrum exercitationem ullam corporis suscipit laboriosam, nisi ut aliquid ex ea commodi consequatur? Quis autem vel eum iure reprehenderit qui in ea voluptate velit esse quam nihil molestiae consequatur, vel illum qui dolorem eum fugiat quo voluptas. Neque porro quisquam est, qui dolorem ipsum quia dolor sit amet, consectetur, adipisci velit, sed quia non numquam eius modi tempora incidunt ut labore et dolore magnam aliquam quaerat voluptatem.</p>
  </div>
</section>

<section class="features">
  <div class="feature" style="left:164px;top:52px;padding:22px 0 0 12px">
    <h3 class="blue">SIMULATION TOOLS</h3>
    <p>Adipiscing Elit, Sed Diam Nonummy Nibh<br>Euismo Tincidunt Ut Laoreet Dolore</p>
  </div>
  <div class="more" style="left:190px;top:166px"><span class="plus">+</span><span class="label">MORE</span></div>

  <div class="feature" style="left:658px;top:52px;padding:18px 14px 0 0;text-align:right">
    <h3 class="dark">HI-TECH WEB PRESENTATIONS</h3>
    <p>Adipiscing Elit, Sed Diam Nonummy Nibh Euismo<br>Tincidunt Ut Laoreet Dolore</p>
  </div>
  <div class="plus-box" style="left:746px;top:60px">+</div>

  <div class="center-brand">
    <div class="sq"></div>
    <div class="name">QORDA</div>
  </div>

  <div class="feature" style="left:164px;top:270px;padding:16px 0 0 2px">
    <h3 class="dark">ENTERPRISE INTRANET SYSTEMS</h3>
    <p>Adipiscing Elit, Sed Diam Nonummy Nibh Euismo<br>Tincidunt Ut Laoreet Dolore</p>
  </div>
  <div class="plus-box" style="left:428px;top:326px">+</div>

  <div class="more" style="left:913px;top:220px"><span class="plus">+</span><span class="label">MORE</span></div>
  <div class="feature" style="left:658px;top:244px;padding:16px 14px 0 0;text-align:right">
    <h3 class="blue">SUPPORTING ENTERPRISE</h3>
    <p>Adipiscing Elit, Sed Diam Nonummy Nibh Euismo<br>Tincidunt Ut Laoreet Dolore</p>
  </div>
</section>

<section class="projects">
  <h2 class="section-title" style="top:36px"><span>RECENT</span> PROJECTS</h2>
  <svg class="divider" style="top:92px" viewBox="0 0 120 12"><line x1="0" y1="6" x2="52" y2="6" stroke="#ccc"/><line x1="68" y1="6" x2="120" y2="6" stroke="#ccc"/><rect x="55" y="1" width="10" height="10" transform="rotate(45 60 6)" fill="none" stroke="#bbb"/></svg>
  <div class="project-strip">
    <span class="strip-arrow" style="left:-8px"></span>
    <span class="strip-arrow" style="right:-8px"></span>
    <div class="project" style="left:42px">
      <div class="shot" role="img" aria-label="Laptop showing a website project" style="background:linear-gradient(135deg,#3b3b3b,#8a6a4a)"></div>
      <p>Lorem Ipsum is simply dummy<br>text of the printing</p>
    </div>
    <div class="project" style="left:245px">
      <div class="shot" role="img" aria-label="Hands typing on a laptop with a studio website" style="background:linear-gradient(135deg,#2a2522,#a07850)"></div>
      <p>Contrary to popular belief,<br>Lorem Ipsum</p>
    </div>
    <div class="project" style="left:448px">
      <div class="shot" role="img" aria-label="Tablet on a desk displaying a mobile app" style="background:linear-gradient(135deg,#c9b9a8,#6a4a3a)"></div>
      <p>There are many variations of<br>passages</p>
    </div>
    <div class="project" style="left:649px">
      <div class="shot" role="img" aria-label="Hand holding a tablet with an application" style="background:linear-gradient(135deg,#9fb8c9,#e2e8ec)"></div>
      <p>It is a long established fact that<br>a reader will be</p>
    </div>
  </div>
</section>

<footer class="site-footer">
  <div class="footer-col" style="left:164px;width:82px">
    <h4>Quick Links</h4>
    <ul class="quick-links">
      <li class="active">HOME</li><li>ABOUT US</li><li>SERVICES</li><li>PROJECTS</li><li>CONTACT US</li>
    </ul>
  </div>
  <div class="footer-col" style="left:316px;width:176px">
    <h4>Contact Information</h4>
    <div class="contact-line">
      <svg width="12" height="16" viewBox="0 0 12 16"><path d="M6 15 C2 9 1 7 1 5.5 A5 5 0 0 1 11 5.5 C11 7 10 9 6 15 Z" fill="#ddd"/><circle cx="6" cy="5.5" r="2" fill="#222"/></svg>
      <span>Qorda Solutions<br>Lorem Ipsum Is The Dummy<br>Content - 948</span>
    </div>
    <div class="contact-line" style="margin-top:26px">
      <svg width="12" height="12" viewBox="0 0 12 12"><path d="M2 1 L4.5 1 L5.5 4 L4 5 Q5 7.5 7 8 L8 6.5 L11 7.5 L11 10 Q5 11 1 3 Z" fill="#ddd"/></svg>
      <span>123-456-7890</span>
    </div>
    <div class="contact-line" style="margin-top:22px">
      <svg width="12" height="10" viewBox="0 0 12 10"><rect x="0" y="1" width="12" height="8" fill="#ddd"/><path d="M0 1 L6 5.5 L12 1" fill="none" stroke="#222"/></svg>
      <span>info@qordasolutions.com</span>
    </div>
  </div>
  <div class="footer-col" style="left:573px;width:250px">
    <h4>Quick Contact</h4>
    <div style="margin-top:16px">
      <div class="field">Name</div>
      <div class="field">Email</div>
      <div class="field msg">Message</div>
      <div class="submit">Submit</div>
    </div>
  </div>
  <div class="footer-brand"><span class="sq"></span><span class="name">QORDA</span></div>
  <div class="social"><span></span><span></span><span></span></div>
</footer>
<div class="copyright">Copyright © 2016 Qorda Solutions. All Rights Reserved.</div>

</body>
</html>
```